Billboard - Cool Garden and Landscape Company (Brand Pack Included)

NEED A PROFESSIONAL BILLBOARD TO ADVERTISE OUR BUSINESS. HAVE MOCKED UP A SAMPLE CONCEPT BUT IT REQUIRES THE ICONS TO BE DEVELOPED TO A PROFESSIONAL STANDARD (I JUST COPIED RANDOM EXAMPLES FROM THE NET)

THE ICONS REPRESENT OUR KEY PRODUCT GROUPS. (These can be redesigned)
BILLBOARD IS 6M X 3M (SEE SPEC FILE ATTACHED) - IMAGE OF THE LOCATION ADDED TO THE FILES.

BRAND GUIDE INCLUDED WITH LOGO FILES

VISIT: https://www.facebook.com/Team.Fern.Crate/
Web: www.ferncrate.co.nz

Target Market(s)

Commuter traffic - busy road - Billboard site is on the left side approx 400m before our street turn off. Age group 30+ Home owners / Builders

Industry/Entity Type

Garden Supply

Font styles to use
Other font styles liked:
• comfortaa

Requirements
Must have
• No change to our logo or brand
• Next left
• Icons for products as per mock up - note these can be redesigned
Nice to have
• Easy to see at a distance
• Clean
• Simple

```html
<!DOCTYPE html>
<html lang="en">
<head>
<meta charset="utf-8">
<title>Fern Crate Billboard</title>
<link rel="stylesheet" href="https://fonts.googleapis.com/css2?family=Open+Sans:wght@400;600;700;800&display=swap">
<style>
  :root {
    --green: #2a9a44;
    --green-dark: #1e7e38;
    --orange: #f7920f;
    --orange-deep: #f08200;
    --ink: #1c1c1c;
    --white: #ffffff;
    --page: #e6e6e6;
  }
  html, body {
    margin: 0;
    width: 1200px;
    height: 1200px;
    overflow: hidden;
    background: var(--page);
    font-family: "Open Sans", Arial, sans-serif;
  }
  .billboard {
    position: absolute;
    left: 50px;
    top: 325px;
    width: 1100px;
    height: 550px;
    box-shadow: 0 10px 30px rgba(0,0,0,0.25);
  }
  .billboard svg { display: block; }
  .brand-name { font-weight: 700; fill: var(--green); font-size: 72px; }
  .arrow-text { font-weight: 800; fill: var(--white); font-size: 46px; }
  .address-text { font-weight: 600; fill: var(--white); font-size: 25px; }
  .product-label { font-weight: 600; fill: var(--ink); font-size: 20px; }
  .web-text { font-weight: 400; fill: var(--white); font-size: 28px; }
  .web-text .web-bold { font-weight: 700; }
  .supplies-text { font-weight: 700; fill: var(--white); font-size: 34px; }
  .icon-disc { fill: var(--orange-deep); stroke: #8fd06a; stroke-width: 2; }
  .icon-glyph { fill: var(--ink); }
</style>
</head>
<body>
<div class="billboard">
<svg width="1100" height="550" viewBox="0 0 1100 550" xmlns="http://www.w3.org/2000/svg">
  <defs>
    <radialGradient id="board-glow" cx="0.6" cy="0.45" r="0.7">
      <stop offset="0" stop-color="#c8ea9a"/>
      <stop offset="0.45" stop-color="#eef8e0"/>
      <stop offset="1" stop-color="#d6f0a6"/>
    </radialGradient>
  </defs>

  <rect class="board-bg" width="1100" height="550" fill="url(#board-glow)"/>

  <g class="brand">
    <rect class="brand-square" x="147" y="80" width="110" height="110" rx="8" fill="var(--green)"/>
    <text class="brand-name" x="202" y="290" text-anchor="middle">FERN</text>
    <text class="brand-name" x="202" y="380" text-anchor="middle">CRATE</text>
  </g>

  <g class="direction-arrow">
    <path d="M401,131 L531,36 L527,96 C600,88 670,88 735,98 L712,178 C650,160 590,158 526,163 L522,213 Z" fill="var(--green)"/>
    <path d="M395,123 L525,30 L521,90 C594,82 664,82 729,92 L706,172 C644,154 584,152 520,157 L516,207 Z" fill="var(--orange)"/>
    <text class="arrow-text" x="585" y="136" text-anchor="middle" transform="rotate(4 585 120)">NEXT LEFT</text>
  </g>

  <g class="address">
    <polygon points="820,0 1045,0 1045,162 932,217 820,162" fill="var(--orange)"/>
    <polygon points="820,0 1045,0 1045,150 932,205 820,150" fill="var(--green-dark)"/>
    <g class="pin-icon" fill="none" stroke="var(--white)" stroke-width="4">
      <path d="M932,78 C920,62 916,55 916,46 A16,16 0 1 1 948,46 C948,55 944,62 932,78 Z"/>
      <circle cx="932" cy="46" r="5"/>
      <ellipse cx="932" cy="80" rx="14" ry="4"/>
    </g>
    <text class="address-text" x="932" y="115" text-anchor="middle">24 Harlow Road</text>
    <text class="address-text" x="932" y="147" text-anchor="middle">(off Bramleys)</text>
  </g>

  <g class="product firewood" transform="translate(455 285)">
    <circle class="icon-disc" r="60"/>
    <g class="icon-glyph">
      <rect x="-30" y="14" width="60" height="11" rx="5" transform="rotate(-12)"/>
      <rect x="-30" y="14" width="60" height="11" rx="5" transform="rotate(12)"/>
      <path d="M0,-38 C8,-24 22,-18 20,0 C18,12 8,16 0,16 C-10,16 -20,10 -20,-2 C-20,-14 -10,-18 -8,-30 C-2,-24 -2,-18 0,-14 C4,-22 4,-30 0,-38 Z"/>
    </g>
    <text class="product-label" y="98" text-anchor="middle">Firewood</text>
    <text class="product-label" y="126" text-anchor="middle">Fire Pellets</text>
  </g>

  <g class="product compost" transform="translate(632 285)">
    <circle class="icon-disc" r="60"/>
    <g class="icon-glyph">
      <rect x="-2" y="-30" width="4" height="42"/>
      <ellipse cx="-12" cy="-14" rx="12" ry="5" transform="rotate(30 -12 -14)"/>
      <ellipse cx="12" cy="-18" rx="12" ry="5" transform="rotate(-30 12 -18)"/>
      <ellipse cx="0" cy="-34" rx="5" ry="10"/>
      <path d="M-38,28 C-24,10 -8,10 0,12 C10,8 26,12 40,28 Z"/>
    </g>
    <text class="product-label" y="98" text-anchor="middle">Compost</text>
    <text class="product-label" y="126" text-anchor="middle">Soil + Mulch</text>
  </g>

  <g class="product stones" transform="translate(808 285)">
    <circle class="icon-disc" r="60"/>
    <g class="icon-glyph">
      <ellipse cx="0" cy="22" rx="34" ry="13"/>
      <ellipse cx="-4" cy="1" rx="22" ry="9"/>
      <ellipse cx="2" cy="-17" rx="14" ry="7"/>
      <ellipse cx="-2" cy="-32" rx="8" ry="5"/>
    </g>
    <text class="product-label" y="98" text-anchor="middle">Decorative</text>
    <text class="product-label" y="126" text-anchor="middle">Stone Aggregates</text>
  </g>

  <g class="product trailers" transform="translate(983 285)">
    <circle class="icon-disc" r="60"/>
    <g class="icon-glyph">
      <path d="M-32,-30 H14 L22,-10 V14 H-32 Z"/>
      <rect x="-26" y="-24" width="12" height="10" fill="var(--orange-deep)"/>
      <rect x="-10" y="-24" width="12" height="10" fill="var(--orange-deep)"/>
      <rect x="7" y="-22" width="8" height="26" fill="var(--orange-deep)"/>
      <rect x="22" y="8" width="20" height="4"/>
      <circle cx="-14" cy="18" r="9"/>
      <circle cx="-14" cy="18" r="3" fill="var(--orange-deep)"/>
    </g>
    <text class="product-label" y="98" text-anchor="middle">Hire Trailers</text>
    <text class="product-label" y="126" text-anchor="middle">Delivery</text>
  </g>

  <g class="footer">
    <rect x="0" y="470" width="460" height="80" fill="var(--green)"/>
    <polygon points="468,445 1100,445 1100,550 412,550" fill="var(--white)"/>
    <polygon points="478,445 1100,445 1100,550 424,550" fill="var(--orange)"/>
    <text class="web-text" x="60" y="519">www.<tspan class="web-bold">ferncrate</tspan>.co.nz</text>
    <text class="supplies-text" x="780" y="509" text-anchor="middle">Garden &amp; Landscape Supplies</text>
  </g>
</svg>
</div>
</body>
</html>
```